New residential property management company

I have a lot of name recognition in our smaller town due to owning a construction company here. I have now started a residential property management company representing landlords and tenants. Just trying to get my name out there and get some rentals to manage!

```html
<!DOCTYPE html>
<html lang="en">
<head>
<meta charset="utf-8">
<title>Halvorsen Property Management — Postcard</title>
<link href="https://fonts.googleapis.com/css2?family=Montserrat:wght@400;500;600;700;800&display=swap" rel="stylesheet">
<style>
  :root {
    --ink: #231f20;
    --panel-dark: #262526;
    --mid-gray: #a7a8aa;
    --soft-gray: #a9a9ab;
    --muted-text: #b3b3b5;
    --paper: #ffffff;
    --backdrop: #eeedeb;
    --pale-box: #efebeb;
    --header-text: #4d4d4f;
  }
  * { margin: 0; padding: 0; box-sizing: border-box; }
  html, body { width: 704px; height: 1200px; overflow: hidden; }
  body {
    background: var(--backdrop);
    font-family: "Montserrat", Arial, sans-serif;
    color: var(--ink);
    position: relative;
  }
  .card {
    position: absolute;
    left: 22px;
    width: 660px;
    height: 468px;
    background: var(--paper);
    overflow: hidden;
    box-shadow: 0 10px 22px rgba(0,0,0,.18);
  }
  .card--front { top: 116px; }
  .card--back { top: 616px; }
  .abs { position: absolute; }

  /* ---------- front ---------- */
  .front-brand { left: 0; top: 0; width: 260px; height: 100px; background: var(--paper); }
  .brand-mark { left: 32px; top: 34px; width: 24px; height: 24px; background: var(--ink); }
  .brand-lockup { left: 66px; top: 30px; width: 170px; }
  .brand-name { font-size: 24px; font-weight: 500; letter-spacing: 0; color: var(--ink); line-height: 1; white-space: nowrap; }
  .brand-sub { margin-top: 5px; text-align: right; font-size: 5.5px; font-weight: 600; letter-spacing: 1.4px; color: var(--ink); white-space: nowrap; }
  .front-panel { left: 0; top: 100px; width: 260px; height: 295px; background: var(--panel-dark); }
  .front-url { left: 0; top: 395px; width: 260px; height: 21px; background: var(--paper); font-size: 10.5px; font-weight: 700; padding-left: 28px; line-height: 21px; }
  .front-footer { left: 0; top: 416px; width: 260px; height: 52px; background: var(--panel-dark); color: #fff; font-size: 9px; font-weight: 500; padding-left: 29px; line-height: 52px; letter-spacing: .2px; }
  .tired { left: 29px; top: 118px; color: #fff; font-size: 17px; font-weight: 600; letter-spacing: .3px; }
  .role-list { left: 29px; top: 147px; list-style: none; color: #fff; font-size: 13.5px; font-weight: 500; letter-spacing: .4px; }
  .role-list li { height: 24.5px; display: flex; align-items: center; gap: 13px; }
  .role-list svg { width: 16px; height: 16px; }
  .help { left: 29px; top: 283px; font-size: 25px; font-weight: 700; line-height: 24.5px; letter-spacing: .4px; }
  .help .lead { color: #fff; }
  .help .rest { color: var(--muted-text); font-weight: 600; }

  .front-strip { left: 260px; top: 0; width: 16px; height: 468px; background: var(--mid-gray); }
  .front-photo { left: 276px; top: 0; width: 384px; height: 262px; background: linear-gradient(180deg, #a3a9ae 0%, #7d858c 45%, #3c4048 70%, #6d6a66 100%); }
  .front-lower { left: 276px; top: 262px; width: 384px; height: 206px; background: var(--mid-gray); }
  .agent-photo { left: 254px; top: 156px; width: 128px; height: 312px; background: linear-gradient(180deg, #3a3536 0%, #141213 40%, #0e0d0d 100%); border-radius: 48px 48px 0 0; }
  .intro-box { left: 370px; top: 264px; width: 290px; height: 149px; background: var(--paper); }
  .intro-name { left: 387px; top: 278px; font-size: 11px; font-weight: 800; }
  .intro-text { left: 387px; top: 292px; width: 258px; font-size: 9.8px; font-weight: 500; line-height: 13px; }
  .intro-cta { left: 387px; top: 351px; font-size: 13.5px; font-weight: 500; line-height: 16px; letter-spacing: .3px; }
  .intro-cta b { font-weight: 800; }
  .intro-rule { left: 387px; top: 411px; width: 47px; height: 3px; background: var(--ink); }
  .front-phone { left: 398px; top: 425px; display: flex; align-items: center; gap: 14px; font-size: 20px; font-weight: 700; color: var(--ink); }
  .front-phone svg { width: 22px; height: 22px; }

  /* ---------- back ---------- */
  .back-left { left: 0; top: 0; width: 255px; height: 468px; background: var(--paper); }
  .services-title { left: 30px; top: 16px; font-size: 25px; font-weight: 800; letter-spacing: .3px; }
  .services-label { left: 30px; top: 51px; height: 14px; background: var(--panel-dark); color: #fff; font-size: 8.5px; font-weight: 500; padding: 0 4px; line-height: 14px; letter-spacing: .3px; }
  .service { left: 30px; width: 222px; }
  .service .num { font-size: 19px; font-weight: 800; line-height: 19px; }
  .service p { font-size: 10px; font-weight: 500; line-height: 13px; margin-top: 1px; }
  .contact-head { left: 30px; top: 366px; font-size: 14.5px; font-weight: 800; }
  .contact-band { left: 0; top: 386px; width: 255px; height: 82px; background: var(--panel-dark); color: #fff; }
  .contact-phone { left: 30px; top: 10px; display: flex; align-items: center; gap: 10px; font-size: 17px; font-weight: 700; }
  .contact-phone svg { width: 16px; height: 16px; }
  .contact-line { left: 30px; display: flex; align-items: center; gap: 12px; font-size: 8.5px; font-weight: 500; }
  .contact-line svg { width: 9px; height: 9px; }

  .back-strip { left: 255px; top: 0; width: 15px; height: 468px; background: var(--mid-gray); }
  .price-head { left: 255px; top: 0; width: 405px; height: 137px; background: var(--soft-gray); }
  .price-copy { left: 298px; top: 19px; color: var(--header-text); font-size: 20px; font-weight: 700; line-height: 18px; letter-spacing: .4px; }
  .price-copy .small { font-weight: 500; font-size: 17px; display: block; margin-top: 4px; }
  .price-copy .amount { font-size: 42px; font-weight: 800; line-height: 40px; display: block; margin-top: 2px; color: var(--ink); }
  .stamp-box { left: 563px; top: 20px; width: 73px; height: 78px; background: var(--paper); }
  .about { left: 298px; top: 157px; width: 340px; font-size: 10px; font-weight: 500; line-height: 13px; }
  .about b { font-weight: 800; }
  .gallery { top: 216px; width: 110px; height: 96px; }
  .gallery--tech { left: 298px; background: linear-gradient(135deg, #5a4a40 0%, #8a8f95 55%, #3f4f72 100%); }
  .gallery--desk { left: 413px; background: linear-gradient(135deg, #d9c9a8 0%, #f3efe6 55%, #c8cfd8 100%); }
  .gallery--meeting { left: 528px; background: linear-gradient(135deg, #cfc7bd 0%, #9a8a7d 50%, #2b2b33 100%); }
  .note-box { left: 298px; top: 325px; width: 340px; height: 120px; background: var(--pale-box); }
</style>
</head>
<body>

<section class="card card--front" aria-label="Postcard front">
  <div class="abs front-brand">
    <div class="abs brand-mark"></div>
    <div class="abs brand-lockup">
      <div class="brand-name">HALVORSEN</div>
      <div class="brand-sub">PROPERTY MANAGEMENT LLC.</div>
    </div>
  </div>

  <div class="abs front-panel"></div>
  <div class="abs tired">TIRED OF BEING THE</div>
  <ul class="abs role-list">
    <li><svg viewBox="0 0 16 16" fill="none" stroke="#fff" stroke-width="1.2"><path d="M1 12h4l4 1 5-3M6 9l3-3 3 3v3H6z"/></svg>LANDLORD</li>
    <li><svg viewBox="0 0 16 16" fill="none" stroke="#fff" stroke-width="1.2"><circle cx="8" cy="5" r="3"/><path d="M3 15v-3a5 5 0 0 1 10 0v3z"/></svg>REPAIRMAN</li>
    <li><svg viewBox="0 0 16 16" fill="none" stroke="#fff" stroke-width="1.2"><circle cx="8" cy="7" r="5"/><path d="M6 15h4M8 4v3h2"/></svg>LEASING AGENT</li>
    <li><svg viewBox="0 0 16 16" fill="none" stroke="#fff" stroke-width="1.2"><rect x="2" y="2" width="9" height="12"/><path d="M4 5h5M4 8h5M4 11h3M12 6h2v8h-4"/></svg>ACCOUNTANT</li>
    <li><svg viewBox="0 0 16 16" fill="none" stroke="#fff" stroke-width="1.2"><circle cx="6" cy="5" r="3"/><path d="M1 15a5 5 0 0 1 10 0M11 9l4 4"/><circle cx="11" cy="9" r="2"/></svg>INSPECTOR</li>
  </ul>
  <div class="abs help">
    <div class="lead">LET US HELP</div>
    <div class="rest">MANAGE</div>
    <div class="rest">YOUR</div>
    <div class="rest">PROPERTY</div>
  </div>
  <div class="abs front-url">www.halvorsenpropertymgmt.com</div>
  <div class="abs front-footer">HALVORSEN PROPERTY MANAGEMENT LLC</div>

  <div class="abs front-strip"></div>
  <div class="abs front-photo" role="img" aria-label="Photo of a dark metal-sided building with two garage doors under a cloudy sky"></div>
  <div class="abs front-lower"></div>
  <div class="abs intro-box"></div>
  <div class="abs agent-photo" role="img" aria-label="Photo of the property manager in black, arms crossed"></div>
  <div class="abs intro-name">I'M MARISSA.</div>
  <div class="abs intro-text">I specialize in virtual real estate management.<br>I am an independent contractor working as a broker's assistant.</div>
  <div class="abs intro-cta">CALL TODAY FOR A <b>FREE</b><br>PROPERTY MANAGEMENT<br>EVALUATION</div>
  <div class="abs intro-rule"></div>
  <div class="abs front-phone">
    <svg viewBox="0 0 24 24" fill="none" stroke="#231f20" stroke-width="2"><path d="M5 3h4l2 5-3 2a12 12 0 0 0 6 6l2-3 5 2v4a2 2 0 0 1-2 2A18 18 0 0 1 3 5a2 2 0 0 1 2-2z"/></svg>
    +1 541-555-0182
  </div>
</section>

<section class="card card--back" aria-label="Postcard back">
  <div class="abs back-left"></div>
  <div class="abs services-title">WHAT WE DO</div>
  <div class="abs services-label">HALVORSEN PROPERTY MANAGEMENT LLC</div>

  <div class="abs service" style="top:85px"><div class="num">01</div><p>Take a pictures off your list so that you<br>can focus on why you started<br>your business</p></div>
  <div class="abs service" style="top:154px"><div class="num">02</div><p>Manage your social media platforms to increase visibility to your target market</p></div>
  <div class="abs service" style="top:210px"><div class="num">03</div><p>Customer service and relations</p></div>
  <div class="abs service" style="top:254px"><div class="num">04</div><p>Finding and screening applicants for<br>job openings</p></div>
  <div class="abs service" style="top:311px"><div class="num">05</div><p>Help the overall growth of your<br>business.</p></div>

  <div class="abs contact-head">CONTACT US</div>
  <div class="abs contact-band">
    <div class="abs contact-phone">
      <svg viewBox="0 0 24 24" fill="none" stroke="#fff" stroke-width="2.2"><path d="M5 3h4l2 5-3 2a12 12 0 0 0 6 6l2-3 5 2v4a2 2 0 0 1-2 2A18 18 0 0 1 3 5a2 2 0 0 1 2-2z"/></svg>
      +1 541-555-0182
    </div>
    <div class="abs contact-line" style="top:35px">
      <svg viewBox="0 0 10 10" fill="#fff"><rect x="0" y="1.5" width="10" height="7"/></svg>
      halvorsenpropertymgmt@mailbox.com
    </div>
    <div class="abs contact-line" style="top:49px">
      <svg viewBox="0 0 10 10" fill="none" stroke="#fff" stroke-width="1"><circle cx="5" cy="5" r="4.2"/><path d="M1 5h8M5 1c-2 2.5-2 5.5 0 8M5 1c2 2.5 2 5.5 0 8"/></svg>
      www.halvorsenpropertymgmt.com
    </div>
  </div>

  <div class="abs back-strip"></div>
  <div class="abs price-head"></div>
  <div class="abs price-copy">
    OUR PROPERTY<br>MANAGEMENT
    <span class="small">STARTS AT</span>
    <span class="amount">$100</span>
  </div>
  <div class="abs stamp-box"></div>

  <div class="abs about"><b>Halvorsen Property Management LLC</b> is based out of Douglas County, Oregon. We are excited to handle every aspect of managing your investment property. Single family, multi family, multi unit dwellings, and apartment complexes.</div>

  <div class="abs gallery gallery--tech" role="img" aria-label="Photo of a technician in a hard hat working at an electrical panel"></div>
  <div class="abs gallery gallery--desk" role="img" aria-label="Photo of hands reviewing paperwork and charts on a desk"></div>
  <div class="abs gallery gallery--meeting" role="img" aria-label="Photo of a couple shaking hands with an agent on a sofa"></div>
  <div class="abs note-box"></div>
</section>

</body>
</html>
```